Occupational Therapist does home accessibility for disabled folks; needs business card design

We need a business card for a company in Portland, Oregon that specializes in making homes accessible, comfortable, and functional for people who are disabled or aging who would like to stay in THEIR home. Our medical background as Occupational Therapists allows us to translate the functional needs of the person into the recommendations for the design of the home remodel.

Target Market(s)

Elderly, children of elderly
People with disabilities, families of people with disabilities

Industry/Entity Type

Business

Contact Information for Business Card

Company name: HomeWell
Name: Karen Dwyer Lopez, OTR/L, CAPS, ECHM
Occupational Therapist, Home Modification & Accessibility Specialist
website: www.homewellsteady.com
email: homewellsteady@mailbright.com
phone: (503)418-2957
CCB #: 384517

Font styles to use
Sans Serif

Requirements
Must have
• My logo
• Easy to read font with contrasting background
• Please list the Services offered: Occupational Therapy, Home safety & accessibility assessments, Home modification consulting, project management
Nice to have
• Friendly, welcoming feel
Should not have
• Dark colored background

```html
<!DOCTYPE html>
<html lang="en">
<head>
<meta charset="UTF-8">
<title>HomeWell Business Card</title>
<link href="https://fonts.googleapis.com/css2?family=Open+Sans:wght@400;600;700&display=swap" rel="stylesheet">
<style>
  :root {
    --orange: #d5801e;
    --orange-deep: #c77417;
    --grey: #8a8a8a;
    --grey-light: #b8b8b8;
    --text-grey: #6b6b6b;
    --white: #ffffff;
    --page: #ecebe8;
  }
  * { margin: 0; padding: 0; box-sizing: border-box; }
  html, body {
    width: 1200px; height: 950px; overflow: hidden;
    background: var(--page);
    font-family: "Open Sans", Arial, sans-serif;
  }
  .sheet {
    position: relative; width: 1200px; height: 950px;
  }
  .card {
    position: absolute; left: 250px;
    width: 700px; height: 400px;
    border-radius: 18px; overflow: hidden;
    box-shadow: 0 6px 18px rgba(0,0,0,0.12);
  }
  .card-front { top: 50px; background: var(--white); }
  .card-back { top: 500px; background: var(--orange); }

  .front-swoosh { position: absolute; inset: 0; }

  .brand {
    position: absolute; display: flex; align-items: center; gap: 12px;
    font-weight: 700; letter-spacing: 0.5px;
  }
  .brand-mark { display: block; }
  .front-brand { left: 52px; top: 170px; color: var(--orange); font-size: 40px; }
  .front-brand .brand-mark { width: 26px; height: 26px; background: var(--orange); }

  .divider {
    position: absolute; left: 318px; top: 40px; width: 1px; height: 215px;
    background: var(--grey-light);
  }

  .contact { position: absolute; left: 345px; top: 34px; }
  .person-name { color: var(--orange); font-size: 27px; font-weight: 700; line-height: 1.2; }
  .credentials { color: var(--orange); font-size: 18px; font-weight: 600; margin-top: 2px; }
  .title { color: var(--text-grey); font-size: 17px; line-height: 1.3; margin-top: 8px; }
  .details { margin-top: 12px; color: var(--text-grey); font-size: 15px; line-height: 1.55; }
  .detail-row { display: flex; align-items: center; gap: 8px; }
  .detail-row svg { width: 14px; height: 14px; flex: none; }

  .website {
    position: absolute; right: 34px; bottom: 22px;
    color: var(--white); font-size: 19px; font-weight: 600; letter-spacing: 0.5px;
  }

  .back-brand {
    left: 0; right: 0; top: 95px; justify-content: center;
    color: var(--white); font-size: 64px;
  }
  .back-brand .brand-mark { width: 40px; height: 40px; background: var(--white); }
  .services { position: absolute; left: 0; right: 0; top: 228px; text-align: center; color: var(--white); }
  .services-heading { font-size: 26px; font-weight: 600; margin-bottom: 10px; }
  .services-list { font-size: 19px; line-height: 1.5; }
</style>
</head>
<body>
<main class="sheet">

  <section class="card card-front">
    <svg class="front-swoosh" viewBox="0 0 700 400" width="700" height="400" aria-hidden="true">
      <path d="M0,318 C120,315 230,280 300,250 C230,300 120,328 0,332 Z" fill="var(--grey)"/>
      <path d="M0,400 V338 C130,334 240,300 310,262 C390,222 430,326 700,322 V400 Z" fill="var(--orange)"/>
    </svg>

    <div class="brand front-brand">
      <span class="brand-mark"></span>
      <span class="brand-name">HomeWell</span>
    </div>

    <div class="divider"></div>

    <div class="contact">
      <div class="person-name">Karen Dwyer Lopez</div>
      <div class="credentials">OTR/L, CAPS, ECHM</div>
      <div class="title">Occupational Therapist<br>Home Modification &amp;<br>Accessibility Specialist</div>
      <div class="details">
        <div class="detail-row">CCB #: 384517</div>
        <div class="detail-row">
          <svg viewBox="0 0 24 24"><path fill="var(--orange)" d="M6.6 10.8a15 15 0 0 0 6.6 6.6l2.2-2.2c.3-.3.7-.4 1-.2 1.1.4 2.3.6 3.6.6.6 0 1 .4 1 1V20c0 .6-.4 1-1 1A17 17 0 0 1 3 4c0-.6.4-1 1-1h3.5c.6 0 1 .4 1 1 0 1.3.2 2.5.6 3.6.1.3 0 .7-.2 1z"/></svg>
          (503)418-2957
        </div>
        <div class="detail-row">
          <svg viewBox="0 0 24 24"><rect x="2" y="5" width="20" height="14" rx="2" fill="var(--orange)"/><path d="M3 6l9 7 9-7" fill="none" stroke="#fff" stroke-width="1.8"/></svg>
          homewellsteady@mailbright.com
        </div>
      </div>
    </div>

    <div class="website">www.homewellsteady.com</div>
  </section>

  <section class="card card-back">
    <div class="brand back-brand">
      <span class="brand-mark"></span>
      <span class="brand-name">HomeWell</span>
    </div>
    <div class="services">
      <div class="services-heading">Services</div>
      <div class="services-list">
        Occupational Therapy | Home safety &amp; accessibility assessments<br>
        Home modification consulting | project management
      </div>
    </div>
  </section>

</main>
</body>
</html>
```